Morvela Aesthetic Doctor

I require an elegant, luxurious looking business card for my aesthetic business. I am a doctor and that will set me aside from competitors. I am planning to provide home and spa based treatments to clients with high expectations. I have attached my logo.

```html
<!DOCTYPE html>
<html lang="en">
<head>
<meta charset="utf-8">
<title>Morvela Aesthetic Doctor – Business Card</title>
<link rel="stylesheet" href="https://fonts.googleapis.com/css2?family=Montserrat:wght@400;500&display=swap">
<style>
  :root {
    --backdrop: #2e2e2e;
    --card: #ffffff;
    --brand-blue: #3b97d3;
    --text-dark: #3a3a3a;
    --band-grey: #a9abae;
    --rule-blue: #7fb8e0;
  }
  * { margin: 0; padding: 0; box-sizing: border-box; }
  html, body {
    width: 1200px; height: 1192px; overflow: hidden;
    background: var(--backdrop);
    font-family: "Montserrat", sans-serif;
  }
  .card {
    position: absolute;
    left: 191px;
    width: 826px;
    height: 472px;
    background: var(--card);
    border-radius: 27px;
    overflow: hidden;
  }
  .card--front { top: 111px; }
  .card--back { top: 615px; }

  .brand {
    position: absolute;
    display: flex;
    align-items: center;
    gap: 18px;
    color: var(--brand-blue);
    font-weight: 400;
  }
  .brand__dot {
    width: 84px; height: 84px;
    border-radius: 50%;
    border: 3px solid var(--brand-blue);
    flex: none;
  }
  .brand__name { line-height: 1.05; }
  .brand__name .big { display: block; font-size: 50px; letter-spacing: 1px; }
  .brand__name .small { display: block; font-size: 24px; letter-spacing: 1.5px; }
  .card--front .brand { left: 394px; top: 52px; }
  .card--back .brand { left: 172px; top: 93px; }
  .card--back .brand__dot { width: 100px; height: 100px; }
  .card--back .brand__name .big { font-size: 60px; }
  .card--back .brand__name .small { font-size: 28px; }

  .person { position: absolute; left: 44px; top: 276px; }
  .person__name { color: var(--brand-blue); font-size: 21px; font-weight: 500; }
  .person__name .creds { font-size: 12px; color: var(--text-dark); font-weight: 400; margin-left: 4px; }
  .person__title { color: var(--text-dark); font-size: 19px; margin-top: 6px; }

  .rule { position: absolute; left: 44px; top: 343px; width: 735px; height: 2px; background: var(--rule-blue); }

  .contacts { position: absolute; left: 44px; top: 354px; list-style: none; }
  .contacts li {
    display: flex; align-items: center; gap: 10px;
    font-size: 18px; color: var(--text-dark); height: 25px;
  }
  .contacts svg { width: 14px; height: 14px; fill: var(--brand-blue); }

  .footer-band { position: absolute; left: 0; top: 432px; width: 826px; height: 40px; }
  .follow {
    position: absolute; left: 592px; top: 436px; height: 30px;
    color: #fff; font-size: 23px; display: flex; align-items: center; gap: 14px;
  }
  .follow .social { width: 18px; height: 18px; border-radius: 50%; background: #fff; }
  .follow .social:first-of-type { margin-left: 6px; }

  .services {
    position: absolute; left: 0; right: 0; top: 333px;
    text-align: center; color: var(--text-dark); font-size: 19.5px; line-height: 26px;
  }
  .services .highlight { color: var(--brand-blue); font-size: 26px; margin-top: 4px; display: block; }
</style>
</head>
<body>

<section class="card card--front">
  <div class="brand">
    <span class="brand__dot"></span>
    <span class="brand__name"><span class="big">MORVELA</span><span class="small">AESTHETIC DOCTOR</span></span>
  </div>

  <div class="person">
    <p class="person__name">Dr Elise Varnholt<span class="creds">MRCPCH MD</span></p>
    <p class="person__title">Australasian Diploma of Aesthetic Medicine</p>
  </div>
  <div class="rule"></div>

  <ul class="contacts">
    <li><svg viewBox="0 0 24 24"><path d="M6.6 10.8a15.1 15.1 0 0 0 6.6 6.6l2.2-2.2a1 1 0 0 1 1-.25 11.4 11.4 0 0 0 3.6.57 1 1 0 0 1 1 1V20a1 1 0 0 1-1 1A17 17 0 0 1 3 4a1 1 0 0 1 1-1h3.5a1 1 0 0 1 1 1c0 1.25.2 2.45.57 3.57a1 1 0 0 1-.25 1z"/></svg>0800 555 018</li>
    <li><svg viewBox="0 0 24 24"><path d="M2 5h20v14H2z"/><path d="M2 5l10 8 10-8" fill="none" stroke="#fff" stroke-width="2"/></svg>elise@morvela.co.nz</li>
    <li><svg viewBox="0 0 24 24"><circle cx="12" cy="12" r="10"/><path d="M2 12h20M12 2c3 3 3 17 0 20M12 2c-3 3-3 17 0 20" stroke="#fff" stroke-width="1.5" fill="none"/></svg>www.morvela.co.nz</li>
  </ul>

  <svg class="footer-band" viewBox="0 0 826 40" preserveAspectRatio="none" aria-hidden="true">
    <path d="M0 8 H470 C492 8 505 3 525 0 H545 V22 H0 Z" fill="var(--band-grey)"/>
    <path d="M0 20 H455 C490 20 505 -2 545 -2" fill="none" stroke="#fff" stroke-width="3"/>
    <path d="M0 23 H455 C490 23 505 1 545 1 H826 V40 H0 Z" fill="var(--brand-blue)"/>
  </svg>
  <div class="follow">follow <span class="social"></span><span class="social"></span></div>
</section>

<section class="card card--back">
  <div class="brand">
    <span class="brand__dot"></span>
    <span class="brand__name"><span class="big">MORVELA</span><span class="small">AESTHETIC DOCTOR</span></span>
  </div>
  <div class="services">
    <p>Dermal injectables - Plasma facials - Microneedling</p>
    <p>Skin boosters - Excessive sweating</p>
    <span class="highlight">Home and Spa Based Treatments</span>
  </div>
</section>

</body>
</html>
```